Kestrel Vale is a new and completely innovative health supplement aimed at males between the ages of 25-60.

The supplement is formulated specifically to address two significant factors that affect men as they age. A reduction in the primary sex hormones and a reduction in their fertility.

I already have the logo design and label designed. I am looking to launch the product in January/February following successful trials.
The website won't need to have selling features inbuilt as I will be going through 3rd party platforms.

The website will however need to direct traffic to websites for a couple of purposes. In total I would expect to have in the region of 5-6 pages in total.

```html
<!DOCTYPE html>
<html lang="en">
<head>
<meta charset="utf-8">
<title>Kestrel Vale – Advanced Multi-Complexed For Men</title>
<link rel="stylesheet" href="https://fonts.googleapis.com/css2?family=Rubik:wght@700;800&family=Raleway:ital,wght@0,400;0,500;0,600;0,700;1,500&display=swap">
<style>
:root{
  --brand:#00b4ec;
  --brand-light:#3cc9f2;
  --brand-deep:#0098d4;
  --ink:#111111;
  --forest:#0d3b35;
  --muted:#9a9a9a;
  --white:#ffffff;
  --line:#dcdcdc;
}
*{margin:0;padding:0;box-sizing:border-box}
html,body{width:1200px;height:4295px;overflow:hidden}
body{position:relative;font-family:'Raleway',sans-serif;color:var(--ink);background:var(--white)}
.abs{position:absolute}
.head{font-family:'Rubik',sans-serif;font-weight:800}
.center{text-align:center}

/* top bar */
.topbar{left:0;top:0;width:1200px;height:37px;background:var(--brand);color:var(--white);font-size:12px}
.topbar .item{position:absolute;top:11px;display:flex;align-items:center;gap:8px}
.topbar .social{position:absolute;top:12px;width:12px;height:12px;border-radius:50%;background:var(--white)}

/* header */
.brand-mark{display:flex;align-items:center;gap:10px}
.brand-mark .dot{width:22px;height:22px;border-radius:50%;background:var(--brand)}
.brand-mark .name{font-family:'Rubik',sans-serif;font-weight:800;font-size:26px;color:var(--ink);line-height:1}
.nav{top:80px;font-size:14px;font-weight:500;color:var(--ink)}
.nav.active{color:var(--brand)}
.btn-dark{background:var(--ink);color:var(--white);font-size:14px;display:flex;align-items:center;justify-content:center}

/* hero */
.hero{left:0;top:143px;width:1200px;height:620px;background:linear-gradient(120deg,#5fd3f5 0%,#22bff0 45%,#3fcaf4 100%)}
.hero-title{left:0;top:280px;width:1200px;font-size:62px;line-height:65px;color:var(--white)}
.hero-copy{left:300px;top:490px;width:600px;font-size:14px;line-height:22px;color:var(--white)}

/* about */
.eyebrow{font-size:14px;font-weight:600;color:var(--brand)}
.section-title{font-size:50px;color:var(--ink);line-height:1}
.body-copy{font-size:14px;line-height:23px;color:var(--muted)}
.btn-brand{background:var(--brand);color:var(--white);font-size:14px;display:flex;align-items:center;justify-content:center}
.bottle{border-radius:40px 40px 34px 34px;background:linear-gradient(90deg,#e7e9ec 0%,#ffffff 45%,#eceef1 100%);box-shadow:0 10px 30px rgba(0,0,0,.12)}

/* features */
.features{left:0;top:1410px;width:1200px;height:228px;background:linear-gradient(90deg,var(--brand-deep),var(--brand-light))}
.feature{position:absolute;top:48px;width:320px;color:var(--white)}
.feature h3{font-family:'Rubik',sans-serif;font-weight:700;font-size:22px;margin:18px 0 8px}
.feature p{font-size:14px;line-height:23px}

/* ingredients */
.ingredient{position:absolute;width:240px;text-align:center}
.ingredient .badge{width:86px;height:86px;border-radius:50%;background:var(--brand);margin:0 auto;display:flex;align-items:center;justify-content:center}
.ingredient h4{font-family:'Rubik',sans-serif;font-weight:700;font-size:22px;margin:14px 0 10px}
.ingredient p{font-size:14px;line-height:23px;color:var(--muted)}

/* video band */
.video-band{left:0;top:2578px;width:1200px;height:435px;background:linear-gradient(120deg,#2ec4f3,#55d0f5 50%,#21bcef)}
.play{border-radius:50%;border:3px solid var(--white);display:flex;align-items:center;justify-content:center}

/* contact */
.form-box{left:638px;top:3127px;width:504px;height:401px;background:var(--brand)}
.field{position:absolute;background:var(--white);border:1px solid #d8eef6;font-size:13px;color:#b5b5b5;padding:10px 14px}

/* reviews */
.reviews{left:0;top:3528px;width:1200px;height:464px;background:linear-gradient(120deg,#22bff0,#4ccff5 60%,#2bc3f2)}
.quote{left:240px;top:3717px;width:720px;font-size:20px;line-height:30px;font-style:italic;font-weight:500;color:var(--white)}

/* footer */
.foot-head{font-size:17px;font-weight:700;color:var(--brand)}
.foot-link{font-size:13px;color:var(--ink)}
.copyright{left:0;top:4233px;width:1200px;height:47px;background:var(--brand);color:var(--white);font-size:12px;display:flex;align-items:center;justify-content:center}
</style>
</head>
<body>

<!-- top bar -->
<div class="abs topbar">
  <div class="item" style="left:50px">
    <svg width="13" height="10" viewBox="0 0 13 10"><rect x="0.5" y="0.5" width="12" height="9" fill="none" stroke="#fff"/><path d="M0.5 0.5 L6.5 5.5 L12.5 0.5" fill="none" stroke="#fff"/></svg>
    hello@kestrelvale.com
  </div>
  <div class="item" style="left:245px">
    <svg width="10" height="13" viewBox="0 0 10 13"><path d="M5 0 C2 0 0 2.2 0 5 C0 8.5 5 13 5 13 C5 13 10 8.5 10 5 C10 2.2 8 0 5 0Z" fill="#fff"/><circle cx="5" cy="5" r="1.8" fill="#00b4ec"/></svg>
    Harbour Lane 42, Westmoor
  </div>
  <span class="social" style="left:1003px"></span>
  <span class="social" style="left:1046px"></span>
  <span class="social" style="left:1089px"></span>
  <span class="social" style="left:1132px"></span>
</div>

<!-- header -->
<div class="abs brand-mark" style="left:55px;top:74px"><span class="dot"></span><span class="name">Kestrel Vale</span></div>
<span class="abs nav active" style="left:338px">HOME</span>
<span class="abs nav" style="left:425px">ABOUT</span>
<span class="abs nav" style="left:518px">BENEFITS</span>
<span class="abs nav" style="left:630px">INGREDIENTS</span>
<span class="abs nav" style="left:770px">CONTACT</span>
<div class="abs btn-dark" style="left:1013px;top:66px;width:132px;height:48px">BUY NOW</div>

<!-- hero -->
<div class="abs hero" role="img" aria-label="Photo of a couple at home, the man holding a supplement bottle, tinted in brand blue"></div>
<h1 class="abs head hero-title center">Advanced<br>Multi-Complexed<br>For Men</h1>
<p class="abs hero-copy center">Lorem ipsum dolor sit amet, consectetur adipiscing elit. Ut elit tellus, luctus nec ullamcorper mattis, pulvinar dapibus leo.</p>
<div class="abs btn-dark" style="left:532px;top:570px;width:135px;height:48px">About Us</div>

<!-- about -->
<p class="abs eyebrow" style="left:104px;top:893px">About The Product</p>
<h2 class="abs head section-title" style="left:104px;top:945px">Kestrel Vale</h2>
<p class="abs body-copy" style="left:104px;top:1023px;width:400px">Lorem ipsum dolor sit amet, consectetuer adipiscing elit. Aenean commodo ligula eget dolor. Aenean massa. Cum sociis natoque penatibus et magnis dis parturient montes, nascetur ridiculus mus.</p>
<p class="abs body-copy" style="left:104px;top:1129px;width:400px">Nulla consequat massa quis enim. Donec pede justo, fringilla vel, aliquet nec, vulputate eget, arcu. In enim justo, rhoncus ut, imperdiet a, venenatis vitae, justo.</p>
<div class="abs btn-brand" style="left:104px;top:1232px;width:153px;height:48px">ORDER NOW</div>
<div class="abs play" style="left:285px;top:1230px;width:52px;height:52px;border-color:var(--brand);border-width:2px">
  <svg width="16" height="18" viewBox="0 0 16 18"><path d="M2 1 L15 9 L2 17Z" fill="#00b4ec"/></svg>
</div>
<span class="abs" style="left:356px;top:1247px;font-size:14px;font-weight:600;color:var(--brand)">Watch Video</span>
<div class="abs bottle" style="left:712px;top:873px;width:260px;height:445px" role="img" aria-label="Kestrel Vale supplement bottle with blue and white label"></div>

<!-- features -->
<div class="abs features">
  <div class="feature" style="left:57px">
    <svg width="40" height="40" viewBox="0 0 40 40" fill="none" stroke="#fff" stroke-width="2"><rect x="6" y="8" width="18" height="26" rx="3"/><rect x="9" y="3" width="12" height="5"/><circle cx="29" cy="28" r="7"/><path d="M11 20 h8 M15 16 v8"/></svg>
    <h3>100% Result</h3>
    <p>Lorem ipsum dolor sit amet, consectetur adipiscing elit. Ut elit tellus, luctus nec.</p>
  </div>
  <div class="feature" style="left:419px">
    <svg width="40" height="40" viewBox="0 0 40 40" fill="none" stroke="#fff" stroke-width="2"><rect x="6" y="17" width="7" height="16"/><path d="M13 19 L19 8 C21 6 24 8 23 11 L22 16 H31 C33 16 34 18 33 20 L30 31 C29 33 28 33 26 33 H13"/></svg>
    <h3>Optimise Sperm Production</h3>
    <p>Lorem ipsum dolor sit amet, consectetur adipiscing elit. Ut elit tellus, luctus nec.</p>
  </div>
  <div class="feature" style="left:781px">
    <svg width="40" height="40" viewBox="0 0 40 40" fill="none" stroke="#fff" stroke-width="2" stroke-linecap="round"><path d="M20 4 v7 M20 29 v7 M4 20 h7 M29 20 h7 M9 9 l5 5 M26 26 l5 5 M31 9 l-5 5 M14 26 l-5 5"/></svg>
    <h3>Optimise Testosterone Level</h3>
    <p>Lorem ipsum dolor sit amet, consectetur adipiscing elit. Ut elit tellus, luctus nec.</p>
  </div>
</div>

<!-- ingredients -->
<p class="abs eyebrow center" style="left:0;top:1755px;width:1200px">WHAT'S IN KESTREL VALE</p>
<h2 class="abs head section-title center" style="left:0;top:1808px;width:1200px">Ingredients</h2>
<p class="abs body-copy center" style="left:310px;top:1876px;width:580px">Lorem ipsum dolor sit amet, consectetuer adipiscing elit. Aenean commodo ligula eget dolor. Aenean massa. Cum sociis</p>

<div class="ingredient" style="left:102px;top:1979px">
  <div class="badge"><svg width="50" height="36" viewBox="0 0 50 36" fill="none" stroke="#fff" stroke-width="3"><rect x="4" y="3" width="16" height="30" rx="8"/><path d="M4 18 h16"/><circle cx="36" cy="22" r="10"/><path d="M29 15 l14 14"/></svg></div>
  <h4>Ingredient</h4>
  <p>Lorem ipsum dolor sit amet, consectetur adipiscing elit.</p>
</div>
<div class="ingredient" style="left:850px;top:1979px">
  <div class="badge"><svg width="50" height="36" viewBox="0 0 50 36" fill="none" stroke="#fff" stroke-width="3"><rect x="4" y="3" width="16" height="30" rx="8"/><path d="M4 18 h16"/><circle cx="36" cy="22" r="10"/><path d="M29 15 l14 14"/></svg></div>
  <h4>Ingredient</h4>
  <p>Lorem ipsum dolor sit amet, consectetur adipiscing elit.</p>
</div>
<div class="ingredient" style="left:102px;top:2242px">
  <div class="badge"><svg width="50" height="36" viewBox="0 0 50 36" fill="none" stroke="#fff" stroke-width="3"><rect x="4" y="3" width="16" height="30" rx="8"/><path d="M4 18 h16"/><circle cx="36" cy="22" r="10"/><path d="M29 15 l14 14"/></svg></div>
  <h4>Ingredient</h4>
  <p>Lorem ipsum dolor sit amet, consectetur adipiscing elit.</p>
</div>
<div class="ingredient" style="left:850px;top:2242px">
  <div class="badge"><svg width="50" height="36" viewBox="0 0 50 36" fill="none" stroke="#fff" stroke-width="3"><rect x="4" y="3" width="16" height="30" rx="8"/><path d="M4 18 h16"/><circle cx="36" cy="22" r="10"/><path d="M29 15 l14 14"/></svg></div>
  <h4>Ingredient</h4>
  <p>Lorem ipsum dolor sit amet, consectetur adipiscing elit.</p>
</div>
<div class="abs bottle" style="left:475px;top:2010px;width:250px;height:420px" role="img" aria-label="Kestrel Vale supplement bottle front view"></div>

<!-- video band -->
<div class="abs video-band" role="img" aria-label="Blue tinted lifestyle photo of a couple, background for the brand video"></div>
<h2 class="abs head center" style="left:0;top:2715px;width:1200px;font-size:52px;color:var(--white)">Revive Your Vertality</h2>
<div class="abs play" style="left:570px;top:2808px;width:60px;height:60px">
  <svg width="18" height="20" viewBox="0 0 18 20"><path d="M3 1 L17 10 L3 19Z" fill="#fff"/></svg>
</div>

<!-- contact -->
<div class="abs" style="left:175px;top:3100px;width:425px;height:428px;background:linear-gradient(180deg,#f3ddcf,#e2b89d 60%,#1f2a44 100%)" role="img" aria-label="Photo of a fit shirtless man holding a Kestrel Vale bottle"></div>
<div class="abs form-box"></div>
<div class="field" style="left:686px;top:3176px;width:199px;height:36px">Name</div>
<div class="field" style="left:895px;top:3176px;width:200px;height:36px">Email</div>
<div class="field" style="left:686px;top:3242px;width:409px;height:36px">Phone Number</div>
<div class="field" style="left:686px;top:3308px;width:409px;height:94px">Message</div>
<div class="abs" style="left:686px;top:3432px;width:409px;height:48px;background:var(--forest);color:var(--white);font-size:14px;display:flex;align-items:center;justify-content:center">ORDER NOW</div>

<!-- reviews -->
<div class="abs reviews" role="img" aria-label="Blue tinted photo of a smiling woman, background for reviews"></div>
<h2 class="abs head center" style="left:0;top:3630px;width:1200px;font-size:50px;color:var(--white)">Client Reviews</h2>
<p class="abs quote center">Lorem ipsum dolor sit amet, consectetur adipiscing elit. Ut elit tellus, luctus nec ullamcorper mattis, pulvinar dapibus leo.</p>
<svg class="abs" style="left:183px;top:3779px" width="12" height="18" viewBox="0 0 12 18"><path d="M10 2 L3 9 L10 16" fill="none" stroke="#fff" stroke-width="2"/></svg>
<svg class="abs" style="left:1003px;top:3779px" width="12" height="18" viewBox="0 0 12 18"><path d="M2 2 L9 9 L2 16" fill="none" stroke="#fff" stroke-width="2"/></svg>
<div class="abs" style="left:538px;top:3796px;width:48px;height:48px;border-radius:50%;background:#e6f7fd"></div>
<span class="abs" style="left:603px;top:3810px;font-size:13px;font-weight:700;color:var(--white)">Marcus Hale</span>
<span class="abs" style="left:606px;top:3833px;font-size:12px;color:#bfeefc">CEO</span>
<span class="abs" style="left:579px;top:3898px;width:5px;height:5px;border-radius:50%;background:#9be3f8"></span>
<span class="abs" style="left:596px;top:3898px;width:5px;height:5px;border-radius:50%;background:#9be3f8"></span>
<span class="abs" style="left:613px;top:3897px;width:7px;height:7px;border-radius:50%;background:var(--ink)"></span>

<!-- footer -->
<div class="abs brand-mark" style="left:70px;top:4063px"><span class="dot"></span><span class="name">Kestrel Vale</span></div>

<p class="abs foot-head" style="left:329px;top:4025px">Quick Links</p>
<span class="abs foot-link" style="left:329px;top:4064px">Home</span>
<span class="abs foot-link" style="left:329px;top:4094px">About Us</span>
<span class="abs foot-link" style="left:329px;top:4124px">Destination</span>
<span class="abs foot-link" style="left:329px;top:4154px">Contact</span>

<p class="abs foot-head" style="left:654px;top:4025px">Other Pages</p>
<span class="abs foot-link" style="left:654px;top:4064px">Privacy &amp; Policy</span>
<span class="abs foot-link" style="left:654px;top:4094px">Terms of Use</span>
<span class="abs foot-link" style="left:654px;top:4124px">Disclaimer</span>
<span class="abs foot-link" style="left:654px;top:4154px">FAQ</span>

<p class="abs foot-head" style="left:870px;top:4025px">Contact Info</p>
<svg class="abs" style="left:870px;top:4070px" width="10" height="13" viewBox="0 0 10 13"><path d="M5 0 C2 0 0 2.2 0 5 C0 8.5 5 13 5 13 C5 13 10 8.5 10 5 C10 2.2 8 0 5 0Z" fill="#00b4ec"/><circle cx="5" cy="5" r="1.8" fill="#fff"/></svg>
<span class="abs foot-link" style="left:891px;top:4064px;width:260px;line-height:21px">18 Linden Row, Eastbrook – 40512</span>
<svg class="abs" style="left:870px;top:4116px" width="12" height="12" viewBox="0 0 12 12"><path d="M2 0 L4.5 0 L5.5 3 L4 4.5 C5 6.5 5.5 7 7.5 8 L9 6.5 L12 7.5 L12 10 C12 11 11 12 10 12 C4.5 12 0 7.5 0 2 C0 1 1 0 2 0Z" fill="#00b4ec"/></svg>
<span class="abs foot-link" style="left:891px;top:4114px">+00 555 0142</span>
<svg class="abs" style="left:870px;top:4145px" width="13" height="10" viewBox="0 0 13 10"><rect x="0.5" y="0.5" width="12" height="9" fill="none" stroke="#00b4ec"/><path d="M0.5 0.5 L6.5 5.5 L12.5 0.5" fill="none" stroke="#00b4ec"/></svg>
<span class="abs foot-link" style="left:891px;top:4143px">care@kestrelvale.com</span>

<div class="abs" style="left:57px;top:4218px;width:1086px;height:1px;background:var(--line)"></div>
<div class="abs copyright">Copyright © 2020. All rights reserved.</div>

</body>
</html>
```